Town's Facebook Cover Photo / Banner

We are launching a new town Facebook Page. The name of the page is:
The Ashvale Crier , its is intended to be the digiatal "town square" for the residence of Ashvale, a very quaint suburan town in NJ.

Would like the words "Town Squre" to be prominent displayed on the Cover photo

Also need to include our Slogan: "Your Community, Your Future, Your Ashvale!"

Target Market(s)

The local Towns People of Ashvale Only

Number of Pages Required

1 page

Requirements
Must have
• The Ashvale Crier Prominently Displayed

```html
<!DOCTYPE html>
<html lang="en">
<head>
<meta charset="utf-8">
<title>Ashvale Crier – Town Square Cover</title>
<link rel="stylesheet" href="https://fonts.googleapis.com/css2?family=Montserrat:wght@300;400;600;700&display=swap">
<style>
  :root {
    --sky-top: #3d5f86;
    --sky-mid: #c98b52;
    --sky-glow: #f3b25a;
    --city-dusk: #5a5560;
    --panel: rgba(22, 30, 48, 0.78);
    --panel-edge: rgba(255, 255, 255, 0.85);
    --text: #ffffff;
  }
  html, body {
    margin: 0;
    padding: 0;
    overflow: hidden;
    background: #ffffff;
  }
  .cover {
    position: relative;
    width: 1200px;
    height: 457px;
    overflow: hidden;
    font-family: "Montserrat", Arial, sans-serif;
    color: var(--text);
  }
  .cover__scene {
    position: absolute;
    inset: 0;
    background:
      linear-gradient(180deg, rgba(0,0,0,0) 55%, rgba(60,55,70,0.85) 80%, #3c3a44 100%),
      radial-gradient(ellipse 60% 45% at 30% 62%, var(--sky-glow) 0%, rgba(243,178,90,0) 70%),
      linear-gradient(100deg, var(--sky-top) 0%, #7c8aa0 22%, var(--sky-mid) 45%, #7a7690 70%, var(--sky-top) 100%);
  }
  .cover__chevron {
    position: absolute;
    inset: 0;
    width: 1200px;
    height: 457px;
  }
  .cover__copy {
    position: absolute;
    left: 648px;
    top: 106px;
    width: 540px;
  }
  .cover__title {
    margin: 0;
    font-size: 50px;
    line-height: 1.1;
    letter-spacing: 0.5px;
    text-transform: uppercase;
  }
  .cover__title-name {
    display: block;
    font-weight: 700;
  }
  .cover__title-sub {
    display: block;
    font-weight: 300;
    letter-spacing: 1px;
  }
  .cover__slogan {
    margin: 14px 0 0;
    font-size: 24px;
    font-weight: 600;
    line-height: 1.4;
  }
</style>
</head>
<body>
  <main class="cover">
    <div class="cover__scene" role="img" aria-label="Photograph of a suspension bridge and city skyline at sunset"></div>

    <svg class="cover__chevron" viewBox="0 0 1200 457" aria-hidden="true">
      <polygon points="644,0 1200,0 1200,457 680,457 527,187" fill="var(--panel)"/>
      <polyline points="634,0 517,187 670,457" fill="none" stroke="var(--panel-edge)" stroke-width="2"/>
    </svg>

    <section class="cover__copy">
      <h1 class="cover__title">
        <span class="cover__title-name">Ashvale Crier -</span>
        <span class="cover__title-sub">Town Square</span>
      </h1>
      <p class="cover__slogan">Your Community, Your Future,<br>Your Ashvale!</p>
    </section>
  </main>
</body>
</html>
```